Social Media Graphics - Copperfield Loop

Create 6-7 individual social media graphics (square size) to encourage folks to join our online course, using either of the text below (only one set of text per graphic:

The Lantern Ridge Method
How to Create a 7-Figure Business From Scratch
Sign Up Today!

Or

The Lantern Ridge Method
Fast-track Your Way to a Multi-Million Business!
Sign Up Today!

For the color scheme of the graphics, use 1 or 2 colors in the color palette attached; or use any colors that look nice with their outfits; AVOID using red, white and blue altogether because it will look like an Independence Day (4th of July) graphic and we don’t want that; make sure the graphics appeal to both men and women

Make sure each graphic contains 1 of the 2 pics attached; and make sure one of the graphics is all TEXT only.

Target Market(s)

men and women looking to make more money

Industry/Entity Type

entrepreneurship

Requirements
Must have
• see the text document attached
Nice to have
• We are open to a nice color design; the color palette colors are not required, especially we don't want red, white and blue used together
Should not have
• AVOID using red, white and blue altogether because it will look like an Independence Day (4th of July) graphic and we dont want that

```html
<!DOCTYPE html>
<html lang="en">
<head>
<meta charset="utf-8">
<title>The Lantern Ridge Method – Sign Up Today</title>
<link rel="stylesheet" href="https://fonts.googleapis.com/css2?family=Montserrat:wght@800;900&family=Mulish:wght@300;800&display=swap">
<style>
  :root {
    --forest: #0f4a3a;
    --forest-deep: #072a20;
    --blush: #f7c6cf;
    --gold: #f0b83e;
    --cream: #f6ead0;
    --button-ink: #0a3327;
  }
  html, body {
    margin: 0;
    padding: 0;
    width: 1200px;
    height: 1200px;
    overflow: hidden;
    background: var(--forest);
  }
  .promo {
    position: relative;
    width: 1200px;
    height: 1200px;
    overflow: hidden;
    background: var(--forest);
  }
  .promo__stripes {
    position: absolute;
    inset: 0;
    width: 1200px;
    height: 1200px;
  }
  .promo__stripes .deep { fill: var(--forest-deep); }
  .promo__stripes .bright { fill: var(--forest); }

  .title {
    margin: 0;
    font-family: "Montserrat", sans-serif;
    font-weight: 900;
    line-height: 1;
  }
  .title span {
    position: absolute;
    left: 118px;
    white-space: nowrap;
  }
  .title__lead {
    top: 216px;
    font-size: 88px;
    font-weight: 800;
    color: var(--blush);
    letter-spacing: -0.02em;
  }
  .title__main {
    top: 312px;
    font-size: 190px;
    color: var(--gold);
    letter-spacing: -0.035em;
  }
  .title__tail {
    top: 524px;
    font-size: 118px;
    color: var(--cream);
    letter-spacing: -0.03em;
  }

  .tagline {
    position: absolute;
    left: 124px;
    top: 676px;
    margin: 0;
    font-family: "Mulish", sans-serif;
    font-weight: 300;
    font-size: 59px;
    line-height: 79px;
    color: var(--blush);
    letter-spacing: -0.01em;
    white-space: nowrap;
  }
  .tagline strong { font-weight: 800; }

  .cta {
    position: absolute;
    left: 127px;
    top: 871px;
    width: 392px;
    height: 100px;
    border-radius: 12px;
    background: var(--gold);
    display: flex;
    align-items: center;
    justify-content: center;
    font-family: "Montserrat", sans-serif;
    font-weight: 800;
    font-size: 33px;
    color: var(--button-ink);
    letter-spacing: 0.01em;
    text-decoration: none;
  }
</style>
</head>
<body>
  <main class="promo">
    <svg class="promo__stripes" viewBox="0 0 1932 1932" preserveAspectRatio="none" aria-hidden="true">
      <polygon class="deep" points="225,0 930,0 486,1932 -219,1932"/>
      <polygon class="bright" points="680,0 810,0 702,470 572,470"/>
      <polygon class="bright" points="321,1560 451,1560 366,1932 236,1932"/>
      <polygon class="deep" points="1015,0 1100,0 787,1360 702,1360"/>
      <polygon class="deep" points="1530,0 1690,0 1596,410 1436,410"/>
      <polygon class="deep" points="1197,1160 1277,1160 1100,1932 1020,1932"/>
      <polygon class="deep" points="2084,0 2244,0 1800,1932 1640,1932"/>
    </svg>

    <h1 class="title">
      <span class="title__lead">THE</span>
      <span class="title__main">LANTERN</span>
      <span class="title__tail">RIDGE METHOD</span>
    </h1>

    <p class="tagline">How to Create a <strong>7-Figure Business</strong><br>From Scratch</p>

    <a class="cta" href="#">SIGN UP TODAY!</a>
  </main>
</body>
</html>
```